Litigation services brochure for PRV.law

improve aesthetics and sync with website color scheme and new staff to emphasize law firm's litigation capabilities. Describe Litigation director, senior attorneys, attorneys, and general capabilities of the firm, licenses to practice, representative trasnactions and litigation experience. Take profile info from individual attorneys listed in the .doc and correlate with www.prv.law profiles for same attorneys. Update photos as needed. I'm not sure what other words I need to add, but this thing says there needs to be more words in my project description. read the brochure attached, and it should be pretty self explanatory. We have lots of info and content on there, we just want it to look better and reflect the updated color scheme of the site (a few of the color bar colors have changed order and color).

Target Market(s)

Houston, Denver

Font styles to use
Serif

Requirements
Must have
• Color scheme that matches www.prv.law
Nice to have
• Better aesthetics and content optimization

```html
<!DOCTYPE html>
<html lang="en">
<head>
<meta charset="utf-8">
<title>Prescott Reyes &amp; Vance — Litigation Brochure</title>
<link rel="stylesheet" href="https://fonts.googleapis.com/css2?family=Cormorant+Garamond:ital,wght@0,500;0,600;0,700;1,500&family=Cormorant+SC:wght@600&family=Lato:wght@400;700&display=swap">
<style>
:root{
  --board:#6e6e6e;
  --ink:#0c0c0c;
  --panel:#1a1a1a;
  --panel-2:#232323;
  --text:#e8e8e8;
  --muted:#b9b9b9;
  --gold:#f2b418;
  --tan:#c9b37a;
  --green:#0e3a1c;
  --orange:#e0731e;
  --maroon:#8a1f3a;
  --rose:#d23a63;
  --serif:'Cormorant Garamond',Georgia,serif;
  --caps:'Cormorant SC','Cormorant Garamond',Georgia,serif;
  --sans:'Lato',Helvetica,Arial,sans-serif;
}
*{margin:0;padding:0;box-sizing:border-box}
html,body{width:977px;height:1200px;overflow:hidden;background:var(--board)}
.board{position:relative;width:977px;height:1200px}
.page{position:absolute;width:387px;height:547px;background:var(--ink);overflow:hidden;box-shadow:0 4px 14px rgba(0,0,0,.45);color:var(--text)}
.page-cover{left:80px;top:34px}
.page-services{left:514px;top:34px}
.page-team{left:298px;top:612px}
.color-bar{position:absolute;left:0;bottom:0;width:100%;height:9px;display:flex}
.color-bar span{flex:1}
.color-bar .c1{background:var(--tan)}.color-bar .c2{background:var(--green)}.color-bar .c3{background:var(--gold)}.color-bar .c4{background:var(--orange)}.color-bar .c5{background:var(--maroon)}
.abs{position:absolute}

/* cover */
.cover-head{left:0;top:0;width:100%;height:98px;background:linear-gradient(#2a2a2a,#161616);text-align:center}
.firm-title{font-family:var(--caps);font-size:23px;letter-spacing:.5px;margin-top:22px;color:#fff;font-weight:600}
.firm-sub{font-family:var(--serif);font-size:15px;letter-spacing:1px;margin-top:4px;color:#fff;font-weight:500}
.cover-photo{left:0;top:98px;width:100%;height:278px;background:radial-gradient(ellipse at 45% 60%,#8a5a3c 0%,#5c3a28 25%,#3b2c22 55%,#1e1a18 100%)}
.cover-body{left:18px;top:396px;width:351px;text-align:center;font-family:var(--serif);color:#ddd}
.cover-copy{font-size:9.7px;line-height:1.45}
.cover-tag{font-style:italic;font-size:7.5px;color:#ccc;margin-top:8px}
.cover-foot{left:0;top:502px;width:100%;height:36px;background:linear-gradient(#303030,#1c1c1c);text-align:center;line-height:36px;font-family:var(--serif);font-size:11px;letter-spacing:3px;color:#ddd}

/* services */
.practice{top:0;width:96.75px;height:112px;padding:20px 6px 0 8px;border-right:1px solid #2b2b2b}
.practice h3{display:flex;align-items:center;gap:5px;font-family:var(--serif);font-weight:600;font-size:8.2px;line-height:1.1;color:#fff;height:20px}
.practice h3 i{flex:0 0 14px;height:14px;border-radius:50%;background:var(--c)}
.practice p{font-family:var(--sans);font-size:4.6px;line-height:1.45;color:var(--muted);margin-top:6px;text-align:justify}
.intro-band{left:0;top:114px;width:100%;height:140px;background:var(--panel)}
.intro-copy{left:16px;top:124px;width:182px;font-family:var(--sans);font-size:5.3px;line-height:1.5;color:#ccc}
.intro-photo{left:208px;top:122px;width:164px;height:118px;background:linear-gradient(135deg,#c9c9c9,#8d8d8d 55%,#5a5a5a)}
.sec-head{left:0;width:100%;background:var(--ink);display:flex;align-items:center;padding-left:14px;gap:6px}
.sec-head i{width:13px;height:11px;background:var(--c);border-radius:2px;flex:0 0 13px}
.sec-head h4{font-family:var(--serif);font-weight:600;font-size:8.5px;letter-spacing:.3px;color:var(--c);white-space:nowrap}
.sec-head p{font-family:var(--sans);font-size:5.2px;color:#ccc;margin-left:4px;line-height:1.4;padding-right:14px}
.sec-body{left:0;width:100%;background:var(--panel-2);font-family:var(--sans);font-size:5.4px;color:#ddd}
.client-grid{display:grid;grid-template-columns:78px 90px 92px 1fr;row-gap:4px;padding:9px 6px 0 20px}
.client-grid b{color:var(--gold);margin-right:3px}
.states{padding:9px 14px 0 18px;line-height:1.7;font-size:6px}
.states b{color:var(--gold)}
.staff-note{padding:8px 14px 0 22px;line-height:1.5;font-size:5.6px}
.offices{display:flex;padding:6px 0 0 22px}
.office{width:128px;line-height:1.4}
.office+.office{border-left:1px solid var(--rose);padding-left:8px}
.office h5{font-family:var(--serif);font-weight:600;font-size:7.5px;color:var(--rose)}
.office p{font-family:var(--serif);font-size:5.6px;color:#ddd}

/* team */
.team-title{left:16px;top:12px;font-family:var(--caps);font-size:15px;color:#fff;font-weight:600}
.portrait{background:linear-gradient(#6a6a6a,#2b2b2b)}
.name{font-family:var(--serif);font-weight:600;font-size:10.5px;color:var(--gold);white-space:nowrap}
.name small{font-size:7px;color:#fff;font-weight:700}
.role{font-family:var(--serif);font-weight:700;font-size:7px;color:#fff}
.contact{font-family:var(--sans);font-size:7px;color:#fff;display:flex;align-items:center;gap:3px}
.contact svg{width:8px;height:8px;fill:none;stroke:var(--gold);stroke-width:1.3}
.lead{font-family:var(--sans);font-weight:700;font-size:5.6px;line-height:1.4;color:#fff}
.bio{font-family:var(--sans);font-size:4.6px;line-height:1.45;color:#cfcfcf;text-align:justify}
.bio p+p{margin-top:3px}
.admit{display:flex;align-items:center;gap:8px}
.admit .pill{background:var(--tan);color:#111;font-family:var(--serif);font-weight:700;font-size:7px;padding:1px 5px;border-radius:7px;white-space:nowrap}
.admit .pill.gold{background:var(--gold)}
.admit p{font-family:var(--sans);font-size:5px;line-height:1.5;color:#fff}
.team-band{left:0;top:258px;width:100%;height:244px;background:var(--panel-2)}
.team-foot{left:0;top:502px;width:100%;height:36px;background:var(--ink);text-align:right;padding-right:24px;line-height:36px;font-family:var(--serif);font-size:10px;letter-spacing:2.5px}
</style>
</head>
<body>
<div class="board">

  <section class="page page-cover">
    <header class="abs cover-head">
      <h1 class="firm-title">Prescott Reyes &amp; Vance</h1>
      <h2 class="firm-sub">ATTORNEYS AT LAW</h2>
    </header>
    <div class="abs cover-photo" role="img" aria-label="Photo of a wooden gavel and brass scales of justice on a desk before law books"></div>
    <div class="abs cover-body">
      <p class="cover-copy">Our firm can represent the entirety of your individual or business’ vertical integration in the market. From oil &amp; gas title research to biotech patents, software copyright and trade secret protection, commercial property contract negotiations, licensing and deal drafting, dispute resolution, and complex litigation…</p>
      <p class="cover-tag">We want to be your only firm.</p>
    </div>
    <div class="abs cover-foot">www.prv.law</div>
    <div class="color-bar"><span class="c1"></span><span class="c2"></span><span class="c3"></span><span class="c4"></span><span class="c5"></span></div>
  </section>

  <section class="page page-services">
    <div class="abs practice" style="left:0;--c:var(--tan)">
      <h3><i></i>Oil, Gas &amp;<br>Other Minerals</h3>
      <p>Our firm has the team and experience ready to help develop and manage your oil and gas interests, from inception through production, operation, diligence, acquisitions, and divestitures.</p>
    </div>
    <div class="abs practice" style="left:96.75px;--c:var(--gold)">
      <h3><i></i>Intellectual<br>Property</h3>
      <p>We’re ready to assist in identifying, protecting, managing, and enforcing intellectual property rights in your business, including patents, trademarks, copyrights, and trade secrets.</p>
    </div>
    <div class="abs practice" style="left:193.5px;--c:var(--orange)">
      <h3><i></i>Residential &amp;<br>Commercial</h3>
      <p>We have the knowledge and staff necessary to assist with your real and commercial property project development, including diligence, transactions, landlord &amp; tenant negotiations, and closings.</p>
    </div>
    <div class="abs practice" style="left:290.25px;border-right:0;--c:var(--maroon)">
      <h3><i></i>Entity and Estate<br>Management</h3>
      <p>PRV is ready to help you maintain, modify, or create an entity or estate plan that works, helping to minimize tax exposure, short and long term, and maintain control over your assets.</p>
    </div>

    <div class="abs intro-band"></div>
    <p class="abs intro-copy">If you create, own, manage, or direct any type of business, you have issues related to our core practice areas. We are ready to handle the entire vertical stack of your company, estate, or property issues. Not merely an energy, IP, or title firm, PRV is structured to handle your intellectual property issues, business operations and transactions, contract drafting and negotiations, acquisition and merger diligence and negotiations, as well as dispute resolution and litigation related to these interests. We want to assist in expanding your business, protecting your ideas, developing and maintaining your rights in property assets, acquiring new businesses and properties, managing your employees, and identifying and protecting against liabilities, infringers, and tortfeasors. With offices in the energy and technology hubs of Houston, TX, and Denver, CO, as well as licenses to practice in many other states across the country, we’re ready.</p>
    <div class="abs intro-photo" role="img" aria-label="Black and white photo of hands signing a document with a pen"></div>

    <div class="abs sec-head" style="top:254px;height:28px;--c:var(--gold)"><i></i><h4>OUR CLIENTS</h4><p>PRV attorneys represent clients in various fields, worldwide</p></div>
    <div class="abs sec-body" style="top:282px;height:42px">
      <div class="client-grid">
        <span><b>1</b>Oil &amp; Gas Operators</span><span><b>2</b>Producers / Manufacturers</span><span><b>3</b>Design / Engineering Firms</span><span><b>4</b>Partnerships and Corporations</span>
        <span><b>5</b>Business Owners and Partners</span><span><b>6</b>Estates Admins and Trustees</span><span><b>7</b>Startups to Large Businesses</span><span><b>8</b>Inventors / Artists / Developers</span>
      </div>
    </div>
    <div class="abs sec-head" style="top:324px;height:38px;--c:var(--gold)"><i></i><h4>OUR ATTORNEYS</h4><p>We have licenses, certifications, and experience necessary to assist regionally, nationally, and globally. Currently, PRV has licenses to practice in</p></div>
    <div class="abs sec-body" style="top:362px;height:32px">
      <p class="states"><b>•</b> Texas <b>•</b> Colorado <b>•</b> Florida <b>•</b> New Mexico <b>•</b> N. Dakota Oklahoma <b>•</b> Oregon Pennsylvania<br><b>•</b> Wyoming <b>•</b> Utah <b>•</b> USPTO <b>•</b> 5th Cir. <b>•</b> US Sup Ct</p>
    </div>
    <div class="abs sec-head" style="top:394px;height:36px;--c:var(--orange)"><i></i><h4>OUR STAFF</h4><p>PRV was founded on principles of transparency and fairness. We want our employees to love working for us so that they will love working for you.</p></div>
    <div class="abs sec-body" style="top:430px;height:32px">
      <p class="staff-note">Our rates are typically lower than our competitors, while our staff is paid more. This means clients get consistent, reliable performance and work product. Not excuses.</p>
    </div>
    <div class="abs sec-head" style="top:462px;height:32px;--c:var(--rose)"><i></i><h4>OUR OFFICES</h4><p>We have offices located in Houston and Denver, with attorneys ready to work with you</p></div>
    <div class="abs sec-body" style="top:494px;height:44px">
      <div class="offices">
        <div class="office"><h5>Bayou Innovation Center</h5><p>220 Milam Ave, Suite 310 Houston, TX 77002</p></div>
        <div class="office"><h5>Front Range Energy Plaza</h5><p>1480 Larimer St, Suite 1200 Denver, CO 80202</p></div>
      </div>
    </div>
    <div class="color-bar"><span class="c1"></span><span class="c2"></span><span class="c3"></span><span class="c4"></span><span class="c5"></span></div>
  </section>

  <section class="page page-team">
    <h2 class="abs team-title">Prescott Reyes &amp; Vance</h2>

    <div class="abs portrait" style="left:19px;top:36px;width:83px;height:80px" role="img" aria-label="Black and white portrait photo of the Senior Counsel"></div>
    <h3 class="abs name" style="left:112px;top:37px">Dalton H. Mercer, <small>J.D., Senior Counsel &amp; Director of Litigation</small></h3>
    <p class="abs contact" style="left:112px;top:53px">
      <svg viewBox="0 0 10 10"><rect x="1" y="2.5" width="8" height="5.5"/><path d="M1 2.5l4 3.2 4-3.2"/></svg>dmercer@prv.law
      <svg viewBox="0 0 10 10" style="margin-left:4px"><path d="M2.5 1l1.8 2-1 1.2a5 5 0 0 0 2.5 2.5l1.2-1 2 1.8-1 1.5C5 9 1 5 1 2z"/></svg>(713) 555-0148 x113
    </p>
    <p class="abs lead" style="left:112px;top:67px;width:262px">Dalton Mercer is Senior Counsel and the Director of Litigation at Prescott Reyes &amp; Vance, PLLC.</p>
    <div class="abs bio" style="left:112px;top:86px;width:262px">
      <p>Dalton has over 30 years of experience in products liability, oil field litigation, construction defects, negligence, maritime, employment, medical, and commercial litigation matters in both state and federal courts. Mr. Mercer is board certified in Personal Injury Trial Law and has served as national product liability counsel for many of his clients. He has represented</p>
    </div>
    <div class="abs bio" style="left:16px;top:120px;width:356px">
      <p>clients and defended their interests in and outside of Texas, including pro hac vice appearances in several states across the country. He holds the highest available peer rating and serves on the board of a local theater company. He has successfully represented clients in complex lost profits claims, wrongful death claims, and costly burn injuries, and has represented defendants in oilfield explosions and fire cases involving multiple wrongful death and serious personal injury claims. Mr. Mercer served for many years as national product liability counsel for a leading franchiser of commercial truck tire retreading equipment, and has been lead counsel for general contractors in complex multi-party wrongful death suits arising from electrocution during construction at a federal facility. He has also served as counsel for oil platform operators in multi-million dollar personal injury and property damage claims resulting from a collision between a fishing boat and mooring buoy. His experience on both the plaintiff and defense sides of high stakes, complicated trials provides immense value to clients in developing trial strategy and litigation talent.</p>
      <p>Dalton Mercer is admitted to practice before the United States District Courts for the Northern, Southern, and Eastern Districts of Texas, all State Courts of Texas, the United States Courts of Appeal for the Fifth and Federal Circuits, the United States Court of Federal Claims, and the Supreme Court of the United States. He is based in the Houston, Texas, office for Prescott Reyes &amp; Vance, PLLC.</p>
    </div>
    <div class="abs admit" style="left:16px;top:229px;width:356px">
      <span class="pill">ADMISSIONS TO PRACTICE</span>
      <p>Texas | U.S. Northern, Western, and Southern Districts of Texas | U.S. Court of Federal Claims<br>U.S. 5th Circuit Court of Appeals, and the U.S. Supreme Court</p>
    </div>

    <div class="abs team-band"></div>
    <div class="abs portrait" style="left:20px;top:276px;width:92px;height:88px" role="img" aria-label="Black and white portrait photo of the Senior Attorney in front of a bookshelf"></div>
    <h3 class="abs name" style="left:121px;top:281px">Warren L. Ashby</h3>
    <p class="abs role" style="left:121px;top:295px">J.D., Senior Attorney, Business &amp; Litigation</p>
    <p class="abs contact" style="left:121px;top:306px">
      <svg viewBox="0 0 10 10"><rect x="1" y="2.5" width="8" height="5.5"/><path d="M1 2.5l4 3.2 4-3.2"/></svg>washby@prv.law
      <svg viewBox="0 0 10 10" style="margin-left:4px"><path d="M2.5 1l1.8 2-1 1.2a5 5 0 0 0 2.5 2.5l1.2-1 2 1.8-1 1.5C5 9 1 5 1 2z"/></svg>(713) 555-0148
    </p>
    <div class="abs bio" style="left:121px;top:320px;width:252px">
      <p>Warren L. Ashby is a Senior Attorney with Prescott Reyes &amp; Vance, PLLC. His practice focuses on the areas of international business law, general business representation, corporate law, commercial litigation, and intellectual property law. Mr. Ashby counsels clients regarding a variety of business transactions, from basic entity formation to complex cross-border acquisitions or licensing agreements, and has advised business clients on legal matters involving many countries across Europe, Asia, Africa, and the Americas.</p>
    </div>
    <div class="abs bio" style="left:16px;top:373px;width:356px">
      <p>As an arbitrator, Mr. Ashby is available for appointment as arbitrator for commercial, international, securities, and intellectual property cases. He is a member of numerous arbitration rosters, including several commercial and international arbitration centers. Mr. Ashby has represented clients with pro hac vice appearances in several states, as well as in federal district courts across the country.</p>
      <p>Warren completed his J.D. cum laude, where he served as student body vice-president. Prior to law school, he attended a state university as a national merit scholar and fellowship scholar. He also served as a legislative aide in the state House of Representatives and Senate.</p>
      <p>Mr. Ashby is a visiting professor at a European university and a former adjunct professor of international commercial arbitration law. He has also coached domestic, international, and securities arbitration teams. Warren is conversational in Italian and English and maintains a working knowledge of Russian and Spanish. He is based in the Houston, Texas, office for Prescott Reyes &amp; Vance, PLLC.</p>
    </div>
    <div class="abs admit" style="left:14px;top:474px;width:356px">
      <span class="pill gold">ADMISSIONS TO PRACTICE</span>
      <p>Texas | U.S. Northern, Western, and Southern Districts of Texas | Fifth Circuit Court of Appeals</p>
    </div>

    <div class="abs team-foot">www.prv.law</div>
    <div class="color-bar"><span class="c1"></span><span class="c2"></span><span class="c3"></span><span class="c4"></span><span class="c5"></span></div>
  </section>

</div>
</body>
</html>
```